Online media outlet needs a blog and logo

A new online blog platform is being established in the UK. The blog will be very similar in layout to www.lumvero.co. It will need to have a main story slider showing three slides and block tiles beneath the slider for additional tiles.

The blog platform will be called 'Brisket Lantern' and will also need a professional looking logo design for the name.

The website should be designed in Word Press.

Industry/Entity Type

Media

Logo Text

Brisket Lantern

Coding

Coded - Design and coding required

Number of Pages Required

3 page

Font styles to use
Other font styles liked:
• Helvetica

Requirements
Must have
• A slider showing three slides. Be similar to Lum V (see previous comment). Be Word Press compatible.

```html
<!DOCTYPE html>
<html lang="en">
<head>
<meta charset="utf-8">
<title>Brisket Lantern — In the UK</title>
<link href="https://fonts.googleapis.com/css2?family=Roboto:wght@300;400;500;700&display=swap" rel="stylesheet">
<style>
:root{
  --ink:#111111;
  --header:#0b0b0b;
  --footer:#1b1b1b;
  --page:#efefef;
  --white:#ffffff;
  --text:#222222;
  --muted:#8a8a8a;
  --body:#666666;
  --line:#dddddd;
}
*{box-sizing:border-box;margin:0;padding:0}
html,body{width:1200px;height:3333px;overflow:hidden}
body{position:relative;background:var(--page);font-family:"Roboto",Helvetica,Arial,sans-serif;color:var(--text)}
.abs{position:absolute}

/* header */
.site-header{left:0;top:0;width:1200px;height:80px;background:var(--header);color:var(--white)}
.editions{left:76px;top:34px;font-size:12px;letter-spacing:.5px}
.editions span{margin:0 8px;color:#888}
.brand{left:0;width:1200px;top:16px;text-align:center}
.brand-name{font-size:21px;font-weight:500;letter-spacing:3px;text-transform:uppercase}
.brand-tag{font-size:10px;letter-spacing:3px;margin-top:2px}
.menu{right:76px;top:32px;font-size:12px;letter-spacing:.5px;display:flex;align-items:center;gap:8px}

/* hero */
.hero{left:0;top:80px;width:1200px;height:575px;overflow:hidden}
.hero-photo{position:absolute;inset:0;background:linear-gradient(100deg,#0f2e44 0%,#1c5873 35%,#2c6f8a 55%,#9fb6c0 72%,#6a8797 100%)}
.hero-shade{position:absolute;inset:0;background:linear-gradient(90deg,rgba(0,0,0,.45),rgba(0,0,0,0) 60%)}
.badge{left:80px;top:246px;background:var(--white);color:var(--ink);font-size:11px;font-weight:700;letter-spacing:.5px;padding:7px 10px}
.hero-title{left:76px;top:294px;width:600px;color:var(--white);font-size:30px;line-height:40px;font-weight:500;white-space:nowrap}
.byline{left:76px;top:441px;color:var(--white);font-size:12px;letter-spacing:.4px;text-transform:uppercase}
.slider-next{left:1093px;top:217px}

/* topics */
.topics{left:0;top:655px;width:1200px;height:78px;background:var(--white)}
.topics a{position:absolute;top:34px;font-size:11px;letter-spacing:.8px;text-transform:uppercase;color:var(--muted);text-decoration:none}
.topics a.current{color:var(--ink);font-weight:700}

/* tiles */
.tile{position:absolute;background:var(--white);overflow:hidden}
.tile .photo{position:absolute;inset:0}
.tile .shade{position:absolute;inset:0;background:linear-gradient(180deg,rgba(0,0,0,0) 50%,rgba(0,0,0,.55))}
.label{position:absolute;left:20px;top:24px;font-size:11px;letter-spacing:.6px;text-transform:uppercase;color:var(--ink)}
.photo-tile .label{color:var(--white)}
.tile-title{position:absolute;left:20px;right:20px;font-size:18px;font-weight:500;line-height:24px}
.text-tile .tile-title{top:62px;color:var(--ink)}
.photo-tile .tile-title{bottom:46px;color:var(--white)}
.excerpt{position:absolute;left:20px;right:30px;top:98px;font-size:12.5px;line-height:22px;color:var(--body)}
.date{position:absolute;left:20px;bottom:20px;font-size:11px;letter-spacing:.5px;text-transform:uppercase;color:var(--ink)}
.photo-tile .date{color:#e5e5e5}
.share{position:absolute;right:22px;bottom:22px;width:12px;height:12px;border-radius:50%;background:var(--ink)}
.photo-tile .share{background:var(--white)}
.big .tile-title{font-size:20px;bottom:50px}

/* briefings */
.briefings{left:0;top:1676px;width:1200px;height:395px;overflow:hidden}
.briefings-photo{position:absolute;inset:0;background:linear-gradient(90deg,#3a3a3a 0%,#151515 30%,#1c1c1c 70%,#444 100%)}
.briefings-title{left:0;width:1200px;top:104px;text-align:center;color:var(--white);font-size:27px;font-weight:300;letter-spacing:2px;text-transform:uppercase}
.briefings-text{left:0;width:1200px;top:156px;text-align:center;color:#e6e6e6;font-size:16px;line-height:21px}
.field{position:absolute;top:246px;height:38px;font-size:12px}
.field-email{left:296px;width:284px;background:var(--white);color:#999;padding:12px 20px}
.field-select{left:596px;width:140px;background:var(--white);color:#333;padding:12px 14px}
.field-select svg{position:absolute;right:14px;top:16px}
.field-button{left:751px;width:153px;border:1px solid #ccc;color:var(--white);text-align:center;padding:12px 0;letter-spacing:.8px;text-transform:uppercase;font-size:11px}

/* loading */
.loading{left:0;width:1200px;top:3013px;text-align:center}
.loading-text{font-size:11px;font-weight:700;letter-spacing:1px;color:var(--ink);margin-top:4px}

/* footer */
.site-footer{left:0;top:3151px;width:1200px;height:182px;background:var(--footer);color:#cfcfcf}
.footer-nav{position:absolute;left:0;width:1200px;top:42px;text-align:center;font-size:11px;letter-spacing:.6px;text-transform:uppercase}
.footer-nav span{margin:0 18px;color:#777}
.copyright{position:absolute;left:0;width:1200px;top:70px;text-align:center;font-size:11px;color:#aaa}
.social{position:absolute;left:0;width:1200px;top:110px;display:flex;justify-content:center;gap:10px}
.social i{display:block;width:30px;height:30px;border-radius:50%;background:var(--white)}
</style>
</head>
<body>

<header class="site-header abs">
  <div class="editions abs">U.K. EDITION<span>|</span>AMERICA EDITION</div>
  <div class="brand abs">
    <div class="brand-name">Brisket Lantern</div>
    <div class="brand-tag">IN THE UK</div>
  </div>
  <div class="menu abs">MENU
    <svg width="14" height="12" viewBox="0 0 14 12"><rect y="0" width="14" height="2" fill="#fff"/><rect y="5" width="14" height="2" fill="#fff"/><rect y="10" width="14" height="2" fill="#fff"/></svg>
  </div>
</header>

<section class="hero abs">
  <div class="hero-photo" role="img" aria-label="Smiling businesswoman holding a tablet in front of a blue glass office building"></div>
  <div class="hero-shade"></div>
  <div class="badge abs">TOP STORY</div>
  <h1 class="hero-title abs">de Finibus Bonorum et Malorum<br>enim ipsam voluptatem quia vol<br>uptas sit aspernatur</h1>
  <div class="byline abs">By Martin Hale</div>
  <svg class="slider-next abs" width="52" height="52" viewBox="0 0 52 52"><circle cx="26" cy="26" r="24" fill="none" stroke="#fff" stroke-width="2"/><path d="M23 17l9 9-9 9" fill="none" stroke="#fff" stroke-width="2.4"/></svg>
</section>

<nav class="topics abs">
  <a class="current" style="left:80px">Current Topics</a>
  <a style="left:262px">Lantern Weekend</a>
  <a style="left:489px">Government</a>
  <a style="left:667px">Politics</a>
  <a style="left:811px">Competition</a>
  <a style="left:984px">Investment</a>
</nav>

<article class="tile photo-tile" style="left:73px;top:782px;width:334px;height:325px">
  <div class="photo" role="img" aria-label="Woman working on a laptop by a window, black and white" style="background:linear-gradient(135deg,#c9c9c9,#6e6e6e 60%,#3a3a3a)"></div>
  <div class="shade"></div>
  <div class="label">Letter</div>
  <h2 class="tile-title">de Finibus Bonorum et Malorum</h2>
  <div class="date">Ledgerly 04 May 2016</div><i class="share"></i>
</article>

<article class="tile text-tile" style="left:433px;top:782px;width:334px;height:325px">
  <div class="label">Enterprise</div>
  <h2 class="tile-title">de Finibus Bonorum et Malorum</h2>
  <p class="excerpt">Sed ut perspiciatis unde omnis iste natus error sit voluptatem accusantium doloremque laudan tium, totam rem aperiam, eaque ipsa quae ab illo inventore veritatis et quasi architecto beatae vitae dicta sunt explicabo.</p>
  <div class="date">Ledgerly 04 May 2016</div><i class="share"></i>
</article>

<article class="tile photo-tile" style="left:793px;top:782px;width:334px;height:325px">
  <div class="photo" role="img" aria-label="Smiling man with glasses seated in a blue armchair" style="background:linear-gradient(135deg,#8a8f96,#3f5a86 55%,#1f2f55)"></div>
  <div class="shade"></div>
  <div class="label">Letter</div>
  <h2 class="tile-title">de Finibus Bonorum et Malorum</h2>
  <div class="date">Ledgerly 04 May 2016</div><i class="share"></i>
</article>

<article class="tile photo-tile" style="left:73px;top:1144px;width:334px;height:216px">
  <div class="photo" role="img" aria-label="Person relaxing on a cloud under a bright blue sky" style="background:linear-gradient(180deg,#1f5aa0,#5e93cf 55%,#e7eef6)"></div>
  <div class="shade"></div>
  <div class="label">Letter</div>
  <h2 class="tile-title">de Finibus Bonorum et Malorum</h2>
  <div class="date">Ledgerly 04 May 2016</div><i class="share"></i>
</article>

<article class="tile text-tile" style="left:73px;top:1391px;width:334px;height:213px">
  <div class="label">Letter</div>
  <h2 class="tile-title">de Finibus Bonorum et Malorum</h2>
  <p class="excerpt">Sed ut perspiciatis unde omnis iste natus error sit voluptatem accusantium doloremque laudan tium, totam rem aperiam, eaque.</p>
  <div class="date">Ledgerly 04 May 2016</div><i class="share"></i>
</article>

<article class="tile photo-tile big" style="left:433px;top:1144px;width:694px;height:460px">
  <div class="photo" role="img" aria-label="Three colleagues looking at a tablet together in a bright office" style="background:linear-gradient(120deg,#d9d3c4,#b7a98d 40%,#6e5a44 70%,#8e7a52)"></div>
  <div class="shade"></div>
  <h2 class="tile-title">Neque porro quisquam est qui dolorem ipsum.</h2>
  <div class="date">Ledgerly 04 May 2016</div><i class="share"></i>
</article>

<section class="briefings abs">
  <div class="briefings-photo" role="img" aria-label="Dark classical stone columns"></div>
  <h2 class="briefings-title abs">Brisket Lantern Email Briefings</h2>
  <p class="briefings-text abs">Sign up to our email briefings to have the best of popular capitalism<br>delivered direct to your inbox.</p>
  <div class="field field-email">Your Email</div>
  <div class="field field-select">Daily<svg width="8" height="5" viewBox="0 0 8 5"><path d="M0 0h8L4 5z" fill="#333"/></svg></div>
  <div class="field field-button">Subscribe</div>
</section>

<article class="tile photo-tile" style="left:73px;top:2140px;width:334px;height:324px">
  <div class="photo" role="img" aria-label="Two businessmen talking in an office" style="background:linear-gradient(135deg,#d8dde2,#8f9aa4 50%,#2f3338)"></div>
  <div class="shade"></div>
  <div class="label">Letter</div>
  <h2 class="tile-title">de Finibus Bonorum et Malorum</h2>
  <div class="date">Ledgerly 04 May 2016</div><i class="share"></i>
</article>

<article class="tile text-tile" style="left:433px;top:2140px;width:334px;height:324px">
  <div class="label">Enterprise</div>
  <h2 class="tile-title">de Finibus Bonorum et Malorum</h2>
  <p class="excerpt">Sed ut perspiciatis unde omnis iste natus error sit voluptatem accusantium doloremque laudan tium, totam rem aperiam, eaque ipsa quae ab illo inventore veritatis et quasi architecto beatae vitae dicta sunt explicabo.</p>
  <div class="date">Ledgerly 04 May 2016</div><i class="share"></i>
</article>

<article class="tile photo-tile" style="left:793px;top:2140px;width:334px;height:324px">
  <div class="photo" role="img" aria-label="Business meeting around a table with documents" style="background:linear-gradient(135deg,#e6e6e6,#a8a8a8 50%,#3c3c3c)"></div>
  <div class="shade"></div>
  <div class="label">Letter</div>
  <h2 class="tile-title">de Finibus Bonorum et Malorum</h2>
  <div class="date">Ledgerly 04 May 2016</div><i class="share"></i>
</article>

<article class="tile photo-tile big" style="left:73px;top:2502px;width:694px;height:462px">
  <div class="photo" role="img" aria-label="Overhead view of a team meeting around a white table with orange chairs" style="background:linear-gradient(135deg,#9a9a9a,#6d6d6d 50%,#4a4a4a)"></div>
  <div class="shade"></div>
  <h2 class="tile-title">Neque porro quisquam est qui dolorem</h2>
  <div class="date">Ledgerly 04 May 2016</div><i class="share"></i>
</article>

<article class="tile text-tile" style="left:793px;top:2502px;width:334px;height:216px">
  <div class="label">Letter</div>
  <h2 class="tile-title">de Finibus Bonorum et Malorum</h2>
  <p class="excerpt">Sed ut perspiciatis unde omnis iste natus error sit voluptatem accusantium doloremque laudan tium, totam rem aperiam, eaque.</p>
  <div class="date">Ledgerly 04 May 2016</div><i class="share"></i>
</article>

<article class="tile photo-tile" style="left:793px;top:2747px;width:334px;height:217px">
  <div class="photo" role="img" aria-label="Business partners shaking hands in a bright office" style="background:linear-gradient(135deg,#e8ecee,#9aa6ad 55%,#39434a)"></div>
  <div class="shade"></div>
  <h2 class="tile-title">de Finibus Bonorum et Malorum</h2>
  <div class="date">Ledgerly 04 May 2016</div><i class="share"></i>
</article>

<div class="loading abs">
  <svg width="56" height="56" viewBox="0 0 56 56"><circle cx="28" cy="28" r="24" fill="none" stroke="#333" stroke-width="3" stroke-dasharray="4 6"/></svg>
  <div class="loading-text">LOADING</div>
</div>

<footer class="site-footer abs">
  <div class="footer-nav">Current Topic<span>|</span>Lantern Weekend<span>|</span>Government<span>|</span>Politics<span>|</span>Competition<span>|</span>Investment</div>
  <div class="copyright">Copyright (c) 2016, Brisket Lantern, All Right Reserved</div>
  <div class="social"><i></i><i></i><i></i><i></i><i></i></div>
</footer>

</body>
</html>
```